Kestrel.vc needs a better website design!

We need a new and better website for Kestrel.vc. We're a Canadian venture capital firm that invests in innovative entrepreneurs. We compete against the following websites: lumora.vc, brightvalefund.ca, osprovc.com, and tessara.vc. We're a diverse group of partners and we're dedicated to the founders we invest in.
Updates

I don’t really like stock photos of random people as part of the website design…so please try to stay away from using those images. Thanks, Owen

Target Market(s)

Canadian entrepreneurs and investors

Industry/Entity Type

Venture capital, finance, investment, entrepreneurship

Coding

Coded - Design and coding required

Number of Pages Required

4 page

Font styles to use
Sans Serif

Colors

Designer to choose colors to be used in the design.

Requirements
Must have
• Clean crisp overall design. Fast and to the point.
Nice to have
• Check out www.kestrel.vc - I did it myself and it is too basic and too wordy.
Should not have
• No stock images with random people in them! Not too wordy or with too many large images that are slow to load.

```html
<!DOCTYPE html>
<html lang="en">
<head>
<meta charset="utf-8">
<title>Kestrel.vc — Tomorrow, Built Today</title>
<link href="https://fonts.googleapis.com/css2?family=Oswald:wght@500;600;700&family=Poppins:wght@400;500;600;700&display=swap" rel="stylesheet">
<style>
:root{
  --green:#7b9a2f;
  --green-dark:#66821f;
  --ink:#1d2326;
  --body:#555b5e;
  --faint:#eef0f0;
  --faint-text:#e7e9ea;
  --footer:#2e383d;
  --footer-line:#46525a;
  --white:#ffffff;
}
*{margin:0;padding:0;box-sizing:border-box}
html,body{width:1200px;height:3104px;overflow:hidden;background:var(--white)}
body{position:relative;font-family:'Poppins',sans-serif;color:var(--ink)}
.abs{position:absolute}

/* header */
.brand{left:96px;top:18px;width:150px;text-align:center}
.brand .dot{width:56px;height:56px;border-radius:50%;background:var(--green);margin:0 auto 6px}
.brand .name{font:700 22px 'Poppins',sans-serif;color:var(--green);letter-spacing:1px}
.nav{left:660px;top:44px;display:flex;gap:26px;font:600 15px 'Poppins',sans-serif;letter-spacing:1px;z-index:3;white-space:nowrap}
.nav a{color:var(--ink);text-decoration:none}
.nav a.active{color:var(--green);border-bottom:2px solid var(--green);padding-bottom:8px}
.nav a.muted{color:#9aa0a3}
.phone-btn{left:1084px;top:28px;width:56px;height:56px;background:var(--white);border:1px solid #d6d9da;display:flex;align-items:center;justify-content:center;z-index:3}

/* decorative vertical name */
.vertical-name{left:1120px;top:110px;transform-origin:left top;transform:rotate(90deg);font:700 170px 'Oswald',sans-serif;color:var(--faint-text);white-space:nowrap;letter-spacing:6px;z-index:0}

/* hero */
.hero-photo{left:380px;top:120px;width:820px;height:540px;background:linear-gradient(160deg,#dfe4e8 0%,#8e99a3 45%,#3b4650 100%);z-index:1}
.hero-frame{left:320px;top:560px;width:280px;height:160px;border:22px solid var(--green);z-index:1}
.hero-card{left:88px;top:180px;width:472px;height:440px;background:var(--white);padding:68px 0 0 28px;z-index:2}
.hero-card h1{font:700 58px/1.08 'Oswald',sans-serif;letter-spacing:3px;text-transform:uppercase}
.hero-card h1 span{color:var(--green)}
.hero-card p{font:400 14px/1.6 'Poppins',sans-serif;color:var(--body);width:380px;margin-top:22px}
.btn{display:inline-block;background:var(--green);color:var(--white);font:600 13px 'Poppins',sans-serif;letter-spacing:1px;padding:16px 28px;text-transform:uppercase}
.hero-card .btn{margin-top:30px}
.scroll-label{left:96px;top:660px;transform-origin:left top;transform:rotate(90deg);font:500 11px 'Poppins',sans-serif;letter-spacing:3px;color:var(--body)}
.scroll-label::before{content:"";display:inline-block;width:40px;height:1px;background:var(--body);vertical-align:middle;margin-right:10px}
.mouse{left:84px;top:776px;width:22px;height:34px;border:2px solid var(--body);border-radius:12px}

/* about */
.about-frame{left:88px;top:878px;width:512px;height:474px;border:22px solid var(--green)}
.about-photo{left:110px;top:900px;width:468px;height:430px;background:linear-gradient(135deg,#c9c8c2 0%,#8a8b86 50%,#4b4d4c 100%)}
.about-text{left:608px;top:970px;width:520px;z-index:2}
.about-text h2{font:600 33px/1.28 'Poppins',sans-serif}
.about-text ol{list-style:none;margin-top:22px;font:400 15px/1.6 'Poppins',sans-serif;color:var(--body);width:500px}
.about-text li{margin-bottom:14px}
.about-text li:first-child::after{content:"";display:block;width:240px;height:2px;background:var(--green);margin-top:12px}

/* portfolio */
.portfolio-panel{left:840px;top:1440px;width:360px;height:880px;background:var(--faint)}
.portfolio-title{left:88px;top:1488px;font:600 32px/1.3 'Poppins',sans-serif;width:420px}
.portfolio-rule{left:520px;top:1516px;width:486px;height:1px;background:#c8cccd}
.arrows{left:1016px;top:1494px;display:flex;gap:6px}
.arrows span{width:42px;height:42px;display:flex;align-items:center;justify-content:center;border:1px solid #c8cccd;background:var(--white)}
.arrows span.on{background:var(--green);border-color:var(--green)}
.portfolio-intro{left:88px;top:1650px;width:260px;font:400 15px/1.55 'Poppins',sans-serif;color:var(--body)}
.portfolio-intro::before{content:"";display:block;width:80px;height:2px;background:var(--green);margin-bottom:18px;margin-top:-20px}
.portfolio-intro .btn{margin-top:22px}
.tile{display:flex;align-items:flex-end;padding:0 24px 22px;font:700 30px 'Oswald',sans-serif;color:var(--white);letter-spacing:2px;text-transform:uppercase;box-shadow:0 18px 40px rgba(0,0,0,.12)}
.tile.teal{left:568px;top:1588px;width:264px;height:300px;background:linear-gradient(180deg,#7fc8b8 0%,#4f9e8f 100%)}
.tile.grey{left:848px;top:1588px;width:264px;height:300px;background:linear-gradient(180deg,#d9dcdd 0%,#8c9397 100%);justify-content:flex-end}
.tile.meeting{left:88px;top:1820px;width:448px;height:392px;background:linear-gradient(160deg,#cfd4d8 0%,#7d858b 55%,#3f464b 100%);justify-content:flex-end}
.tile.purple{left:568px;top:1912px;width:544px;height:300px;background:linear-gradient(120deg,#3a1a6b 0%,#6a2a9c 55%,#2b6fb3 100%);justify-content:flex-end}

/* contact */
.contact-band{left:0;top:2380px;width:760px;height:300px;background:var(--faint)}
.contact-title{left:140px;top:2440px;font:500 44px/1.25 'Oswald',sans-serif;text-transform:uppercase;width:440px;letter-spacing:1px}
.contact-title span{color:var(--green)}
.email-field{left:640px;top:2522px;width:412px;height:42px;border:1px solid #b9bdbf;background:var(--white);display:flex;align-items:center;justify-content:space-between;padding:0 16px;font:500 11px 'Poppins',sans-serif;letter-spacing:1px;color:var(--body)}

/* footer */
.footer{left:0;top:2740px;width:1200px;height:364px;background:var(--footer);color:#d6dadc}
.footer .brand{left:180px;top:60px}
.footer h4{font:700 18px 'Poppins',sans-serif;color:var(--white);letter-spacing:1px;margin-bottom:14px;text-transform:uppercase}
.footer ul{list-style:none;font:400 13px/1.85 'Poppins',sans-serif;text-transform:uppercase}
.col-links{left:368px;top:60px}
.col-contact{left:592px;top:60px;width:260px}
.col-contact li{display:flex;gap:10px;align-items:flex-start;text-transform:none;line-height:1.5;margin-bottom:12px}
.col-social{left:910px;top:60px}
.social{display:flex;gap:12px}
.social span{width:22px;height:22px;border-radius:50%;background:#d6dadc}
.footer-rule{left:180px;top:316px;width:840px;height:1px;background:var(--footer-line)}
.copyright{left:0;top:326px;width:1200px;text-align:center;font:400 12px 'Poppins',sans-serif;color:#aab1b4}
</style>
</head>
<body>

<div class="abs vertical-name">KESTREL.VC</div>

<header>
  <div class="abs brand"><div class="dot"></div><div class="name">KESTREL.VC</div></div>
  <nav class="abs nav">
    <a class="active" href="#">HOME</a><a href="#">WHAT</a><a href="#">HOW</a><a href="#">WHO</a><a class="muted" href="#">PORTFOLIO</a>
  </nav>
  <div class="abs phone-btn">
    <svg width="20" height="20" viewBox="0 0 24 24"><path d="M6.6 10.8a15 15 0 0 0 6.6 6.6l2.2-2.2c.3-.3.7-.4 1-.2 1.1.4 2.3.6 3.6.6.6 0 1 .4 1 1V20c0 .6-.4 1-1 1A17 17 0 0 1 3 4c0-.6.4-1 1-1h3.5c.6 0 1 .4 1 1 0 1.3.2 2.5.6 3.6.1.3 0 .7-.2 1z" fill="#1d2326"/></svg>
  </div>
</header>

<section>
  <div class="abs hero-photo" role="img" aria-label="Upward view of glass office towers against the sky"></div>
  <div class="abs hero-frame"></div>
  <div class="abs hero-card">
    <h1>Tomorrow,<br>Built <span>Today</span></h1>
    <p>Kestrel.vc is a venture capital firm that invests in innovative, early-stage technology companies in Western Canada, focused on B2B and SaaS markets.</p>
    <a class="btn" href="#">Find out more</a>
  </div>
  <div class="abs scroll-label">SCROLL</div>
  <div class="abs mouse"></div>
</section>

<section>
  <div class="abs about-frame"></div>
  <div class="abs about-photo" role="img" aria-label="Founders working together at a laptop in a bright office"></div>
  <div class="abs about-text">
    <h2>We are serial entrepreneurs and venture capital investors who provide:</h2>
    <ol>
      <li>1. Mentoring and strategic advice to help you grow your company quickly and efficiently</li>
      <li>2. Investor introductions to help you raise additional follow-on funding for your startup</li>
    </ol>
  </div>
</section>

<section>
  <div class="abs portfolio-panel"></div>
  <h2 class="abs portfolio-title">Check out our innovative portfolio companies!</h2>
  <div class="abs portfolio-rule"></div>
  <div class="abs arrows">
    <span><svg width="12" height="12" viewBox="0 0 12 12"><path d="M8 1 3 6l5 5" fill="none" stroke="#1d2326" stroke-width="2"/></svg></span>
    <span class="on"><svg width="12" height="12" viewBox="0 0 12 12"><path d="m4 1 5 5-5 5" fill="none" stroke="#fff" stroke-width="2"/></svg></span>
  </div>
  <div class="abs portfolio-intro">
    <p>Questions about how we make our venture capital investments?</p>
    <a class="btn" href="#">How we make</a>
  </div>
  <div class="abs tile teal" role="img" aria-label="Portfolio founder portrait on a teal background">FINOVA</div>
  <div class="abs tile grey" role="img" aria-label="Portfolio founder portrait on a light grey background">FINOVA</div>
  <div class="abs tile meeting" role="img" aria-label="Team meeting around a conference table">TESTLOOP</div>
  <div class="abs tile purple" role="img" aria-label="Two founders in front of a colourful gaming backdrop">GAMERIA.GG</div>
</section>

<section>
  <div class="abs contact-band"></div>
  <h2 class="abs contact-title">Contact us today if you <span>have what we're looking for.</span></h2>
  <div class="abs email-field">ENTER EMAIL ADDRESS
    <svg width="26" height="10" viewBox="0 0 26 10"><path d="M0 5h24M20 1l4 4-4 4" fill="none" stroke="#1d2326" stroke-width="1.5"/></svg>
  </div>
</section>

<footer class="abs footer">
  <div class="abs brand"><div class="dot"></div><div class="name">KESTREL.VC</div></div>
  <div class="abs col-links">
    <h4>Quick Links</h4>
    <ul><li>LP Login</li><li>Global</li><li>Founder Resources</li><li>Events</li><li>Press Kit</li><li>Contact Us</li></ul>
  </div>
  <div class="abs col-contact">
    <h4>Contact Us</h4>
    <ul>
      <li><svg width="14" height="16" viewBox="0 0 14 18"><path d="M7 0a7 7 0 0 0-7 7c0 5 7 11 7 11s7-6 7-11a7 7 0 0 0-7-7zm0 10a3 3 0 1 1 0-6 3 3 0 0 1 0 6z" fill="#d6dadc"/></svg>1515 Maple Ridge Road,<br>Suite 210, Calgary, AB T2P 0K1</li>
      <li><svg width="14" height="14" viewBox="0 0 24 24"><path d="M6.6 10.8a15 15 0 0 0 6.6 6.6l2.2-2.2c.3-.3.7-.4 1-.2 1.1.4 2.3.6 3.6.6.6 0 1 .4 1 1V20c0 .6-.4 1-1 1A17 17 0 0 1 3 4c0-.6.4-1 1-1h3.5c.6 0 1 .4 1 1 0 1.3.2 2.5.6 3.6.1.3 0 .7-.2 1z" fill="#d6dadc"/></svg>Phone: (403) 555-0142</li>
      <li><svg width="14" height="12" viewBox="0 0 16 12"><rect x="0.5" y="0.5" width="15" height="11" fill="none" stroke="#d6dadc"/><path d="m1 1 7 6 7-6" fill="none" stroke="#d6dadc"/></svg>Email: info@kestrel.vc</li>
    </ul>
  </div>
  <div class="abs col-social">
    <h4>Social</h4>
    <div class="social"><span></span><span></span></div>
  </div>
  <div class="abs footer-rule"></div>
  <div class="abs copyright">Copyright © 2021 Kestrel.vc - All Rights Reserved</div>
</footer>

</body>
</html>
```